UI/UX Design for AI Photo-to-Video Web Platform (Figma)

I am looking for a modern, high-converting redesign for my Next.js-based web platform. The service allows users to transform old photos into vibrant memories using AI. The design needs to be clean, intuitive, and "mobile-ready" (responsive).
Key Features to Visualize on the Homepage:
Photo Restoration & Colorization: A clear "before/after" visual showing a black-and-white photo turning into a high-quality color photo.
Photo-to-Video Animation: A visual representation of how both B&W and color photos are transformed into dynamic video clips.
Story Creation: A section showing how these photos and videos are combined into a single "Story Video" with background music.
Scope of Work:
Homepage Redesign: A hero section with the core value proposition and a visual walkthrough of the process.
Service/Internal Pages: Redesigning the functional pages where users upload files and manage their projects.
Responsive Design: While the focus is desktop, the layout must be designed with a "Mobile-First" mindset for easy porting to a mobile app later.
Technical Requirements for the Designer:
Tool: Must be designed in Figma.
Structure: Use Figma Auto Layout and Components for all elements (buttons, inputs, cards).
Design System: Provide a clear style guide (Typography, Color Palette, Spacing).
Assets: All icons should be in SVG format.
Style Preference:
Modern, sleek, and trustworthy.
Since the product is about "memories," the vibe should be emotional yet technologically advanced (AI-driven).

```html
<!DOCTYPE html>
<html lang="en">
<head>
<meta charset="utf-8">
<title>tintmemo.ai — Photo and Video Enhancer</title>
<link href="https://fonts.googleapis.com/css2?family=Lexend:wght@400;500;600;700&family=Montserrat:wght@400;500;600&display=swap" rel="stylesheet">
<style>
  :root{
    --ink:#0d2a16;
    --text:#2b2b2b;
    --muted:#6b6b6b;
    --accent:#e08600;
    --accent-soft:#fdf1dc;
    --accent-line:#f0b55a;
    --line:#ececec;
    --panel:#f7f6f4;
    --page:#ffffff;
  }
  *{box-sizing:border-box;margin:0;padding:0}
  html,body{width:733px;height:1200px;overflow:hidden;background:var(--page)}
  body{font-family:"Montserrat",sans-serif;color:var(--text)}
  .site-header{height:58px;display:flex;align-items:center;justify-content:space-between;padding:0 34px;border-bottom:1px solid var(--line)}
  .brand{font-family:"Lexend",sans-serif;font-weight:600;font-size:19px;color:var(--ink);letter-spacing:-.2px}
  .account{display:flex;align-items:center;gap:18px;font-size:10.5px;color:var(--text)}
  .account-item{display:flex;align-items:center;gap:6px}
  .coin{width:14px;height:14px;border-radius:50%;background:var(--accent-line)}
  .storage-icon{width:14px;height:10px;border-radius:2px;background:var(--accent-line)}
  .quota{color:var(--muted)}
  .avatar{width:20px;height:20px;border-radius:50%;background:linear-gradient(135deg,#9a9a9a,#5c5c5c)}
  .caret{width:0;height:0;border-left:4px solid transparent;border-right:4px solid transparent;border-top:4px solid #999;margin-left:6px}
  .user{font-weight:600}

  .hero{text-align:center;padding-top:38px}
  .hero-title{font-family:"Lexend",sans-serif;font-weight:700;font-size:41px;color:var(--ink);letter-spacing:-.5px}
  .hero-lead{margin:18px auto 0;width:560px;font-size:13.5px;line-height:1.6;color:var(--muted)}
  .mode-tabs{display:inline-flex;gap:4px;margin-top:26px;padding:5px;border-radius:24px;background:var(--accent-soft);border:1px solid #f6dfb7}
  .mode-tab{display:flex;align-items:center;gap:7px;padding:9px 14px;border-radius:20px;font-family:"Lexend",sans-serif;font-size:12.5px;color:var(--ink)}
  .mode-tab.is-active{background:#fff;color:var(--accent);box-shadow:0 1px 3px rgba(0,0,0,.06)}
  .tab-icon{width:14px;height:12px;border-radius:2px;background:var(--accent)}
  .tab-icon.dark{background:#5a3a1c}
  .tab-icon.round{border-radius:50%;width:13px;height:13px;background:#5a3a1c}

  .workspace{display:flex;gap:16px;width:600px;margin:34px auto 0;height:270px}
  .compare{position:relative;flex:1;border-radius:12px;overflow:hidden}
  .compare-before{position:absolute;inset:0 50% 0 0;background:linear-gradient(160deg,#c9c7c1,#7d7a74 70%,#56534f)}
  .compare-after{position:absolute;inset:0 0 0 50%;background:linear-gradient(160deg,#e8c27a,#7a2f36 45%,#2c3358 75%,#c9a27a)}
  .compare-divider{position:absolute;left:50%;top:0;bottom:0;width:2px;background:#fff;transform:translateX(-1px)}
  .compare-handle{position:absolute;left:50%;top:50%;width:30px;height:30px;margin:-15px 0 0 -15px;border-radius:50%;background:rgba(70,70,70,.75)}
  .compare-label{position:absolute;bottom:12px;padding:4px 10px;border-radius:5px;background:rgba(40,40,40,.55);color:#fff;font-size:10px;font-weight:600}
  .compare-label.before{left:10px}
  .compare-label.after{right:10px}

  .dropzone{flex:1;background:var(--panel);border-radius:12px;padding:14px}
  .dropzone-inner{height:100%;border:1.5px dashed var(--accent-line);border-radius:8px;display:flex;flex-direction:column;align-items:center;justify-content:center;text-align:center}
  .dropzone-title{margin-top:22px;font-family:"Lexend",sans-serif;font-size:14px;color:var(--ink)}
  .dropzone-note{margin-top:5px;font-size:8.5px;color:var(--muted)}
  .upload-button{margin-top:22px;display:inline-flex;align-items:center;gap:8px;padding:10px 26px;border-radius:20px;background:var(--accent);color:#fff;font-family:"Lexend",sans-serif;font-size:12px}

  .legal{text-align:center;margin-top:26px;font-size:10.5px;color:var(--muted)}
  .legal a{color:var(--accent);font-weight:600;text-decoration:none}

  .benefits{margin-top:30px;border-top:1px solid var(--line);border-bottom:1px solid var(--line);height:56px;display:flex;align-items:center;justify-content:center;gap:54px;font-family:"Lexend",sans-serif;font-size:12px;color:var(--ink)}
  .benefit{display:flex;align-items:center;gap:9px}
  .benefit-icon{width:18px;height:18px;border-radius:50%;background:var(--accent-soft);display:flex;align-items:center;justify-content:center}

  .how{text-align:center;padding-top:52px}
  .section-title{font-family:"Lexend",sans-serif;font-weight:700;font-size:36px;color:var(--ink)}
  .steps{display:flex;gap:14px;width:600px;margin:34px auto 0;text-align:left}
  .step-card{flex:1;height:262px;border:1px solid var(--line);border-radius:10px;padding:18px 16px}
  .step-art{width:72px;height:70px;margin:0 auto 28px;border-radius:14px;background:linear-gradient(150deg,#fbd37a,#e9a53a)}
  .step-art.cloud{border-radius:36px 36px 18px 18px}
  .step-num{font-size:10px;font-weight:600;color:var(--accent)}
  .step-title{margin-top:8px;font-family:"Lexend",sans-serif;font-weight:600;font-size:15px;color:var(--ink)}
  .step-text{margin-top:12px;font-size:11px;line-height:1.6;color:var(--text)}
</style>
</head>
<body>
  <header class="site-header">
    <div class="brand">tintmemo.ai</div>
    <div class="account">
      <div class="account-item"><span class="coin"></span>4740 credits</div>
      <div class="account-item"><span class="storage-icon"></span><b>114MB</b><span class="quota">/ 1.0 GB</span></div>
      <div class="account-item"><span class="avatar" role="img" aria-label="User avatar"></span><span class="user">Mira Osten</span><span class="caret"></span></div>
    </div>
  </header>

  <section class="hero">
    <h1 class="hero-title">Ai Photo and Video Enhancer</h1>
    <p class="hero-lead">Give your photos more depth and texture by using our AI. More natural tones and details will be apparent without the overly processed appearance.</p>
    <nav class="mode-tabs">
      <span class="mode-tab is-active"><span class="tab-icon"></span>Images</span>
      <span class="mode-tab"><span class="tab-icon dark"></span>Video Animations</span>
      <span class="mode-tab"><span class="tab-icon round"></span>Studio</span>
    </nav>

    <div class="workspace">
      <div class="compare">
        <div class="compare-before" role="img" aria-label="Black and white vintage photo of a man holding a child"></div>
        <div class="compare-after" role="img" aria-label="The same photo restored in colour"></div>
        <div class="compare-divider"></div>
        <div class="compare-handle">
          <svg width="30" height="30" viewBox="0 0 30 30"><path d="M13 10l-5 5 5 5zM17 10l5 5-5 5z" fill="#fff"/></svg>
        </div>
        <span class="compare-label before">Before</span>
        <span class="compare-label after">After</span>
      </div>
      <div class="dropzone">
        <div class="dropzone-inner">
          <svg width="40" height="44" viewBox="0 0 40 44">
            <path d="M6 2h20l12 12v26a2 2 0 0 1-2 2H6a2 2 0 0 1-2-2V4a2 2 0 0 1 2-2z" fill="#fff" stroke="#f0b55a" stroke-width="1.5"/>
            <path d="M26 2v12h12" fill="none" stroke="#f0b55a" stroke-width="1.5"/>
            <rect x="10" y="18" width="20" height="16" rx="2" fill="#f7b23b"/>
            <path d="M10 34l7-9 5 6 3-3 5 6z" fill="#e06b00"/>
          </svg>
          <div class="dropzone-title">Drag and drop images here</div>
          <div class="dropzone-note">Maximum 20 images • 100MB total • JPG, PNG, GIF, TIFF up to 10MB each</div>
          <span class="upload-button">Upload files
            <svg width="11" height="12" viewBox="0 0 11 12"><path d="M1 1h9M5.5 11V4M2.5 6.5l3-3 3 3" fill="none" stroke="#fff" stroke-width="1.5" stroke-linecap="round"/></svg>
          </span>
        </div>
      </div>
    </div>

    <p class="legal">By uploading a file, you agree to our <a href="#">Terms of Use</a> and <a href="#">Privacy Policy</a>.</p>
  </section>

  <div class="benefits">
    <div class="benefit"><span class="benefit-icon"><svg width="10" height="11" viewBox="0 0 10 11"><path d="M5 1l4 1.5v3C9 8 7 9.5 5 10 3 9.5 1 8 1 5.5v-3z" fill="none" stroke="#e08600" stroke-width="1.2"/><path d="M3.2 5.5l1.3 1.3 2.3-2.5" fill="none" stroke="#e08600" stroke-width="1.2"/></svg></span>Focused on privacy</div>
    <div class="benefit"><span class="benefit-icon"><svg width="10" height="10" viewBox="0 0 10 10"><rect x="1" y="1" width="8" height="8" rx="2" fill="none" stroke="#e08600" stroke-width="1.2"/><path d="M3 5.2l1.4 1.4L7 3.8" fill="none" stroke="#e08600" stroke-width="1.2"/></svg></span>User-friendly</div>
    <div class="benefit"><span class="benefit-icon"><svg width="11" height="10" viewBox="0 0 11 10"><path d="M1 3h3M0.5 5h3M1 7h3M6 1L5 5h2l-1 4 4-5H8l1-3z" fill="none" stroke="#e08600" stroke-width="1.1" stroke-linejoin="round"/></svg></span>Fast and accurate</div>
  </div>

  <section class="how">
    <h2 class="section-title">How It Works</h2>
    <div class="steps">
      <article class="step-card">
        <div class="step-art" role="img" aria-label="Illustration of a hand selecting an option in a window"></div>
        <div class="step-num">Step 1</div>
        <h3 class="step-title">Select enhancement type</h3>
        <p class="step-text">Lorem ipsum dolor sit amet consectetur. Nec sollicitudin dignissim enim neque habitant.</p>
      </article>
      <article class="step-card">
        <div class="step-art cloud" role="img" aria-label="Illustration of a cloud with an upload arrow"></div>
        <div class="step-num">Step 2</div>
        <h3 class="step-title">Upload files</h3>
        <p class="step-text">Facilisis quis tempus sit eget egestas sagittis sed. Mollis eget viverra feugiat diam et aliquet tellus.</p>
      </article>
      <article class="step-card">
        <div class="step-art" role="img" aria-label="Illustration of a sparkling file with a download arrow"></div>
        <div class="step-num">Step 3</div>
        <h3 class="step-title">Download results</h3>
        <p class="step-text">Malesuada tempus vitae tellus fermentum posuere lectus scelerisque.</p>
      </article>
    </div>
  </section>
</body>
</html>
```